Marlowes a fast food restaurant need a flag designed, has the images uploaded

I have the logo and images, need images to be resized and text added under the images.
This is a two sided flag and to be printed with flagmerto.com,
I need the flag to have the logo on one side and the food images on the other side with identifier underneath it
like
Paratha Wrap
Rice Bowl
Nanini
Naan Pizza

The images might need some modifications and resizing. I will also need to be placed to make the biggest impact on the design

Target Market(s)

Street sign

Industry/Entity Type

Fast Food Restaurant

Font styles to use
Sans Serif

Colors

Designer to choose colors to be used in the design.

Requirements
Must have
• It must have clarity and sharpness
Nice to have
• border highlight and make any changes that could make it better. I ma open to suggestions.
Should not have
• misalignment. smudges, pixelisation

```html
<!DOCTYPE html>
<html lang="en">
<head>
<meta charset="utf-8">
<title>Marlowes Feather Flags</title>
<link rel="stylesheet" href="https://fonts.googleapis.com/css2?family=Open+Sans:wght@700&family=Rosario:wght@400&display=swap">
<style>
  :root {
    --page-bg: #eef0f1;
    --flag-orange: #e8401f;
    --flag-brown: #7a2e1a;
    --panel-dark: #1f1417;
    --cream-top: #fde0bf;
    --cream-bottom: #fdf8d8;
    --badge-green: #d4e6a0;
    --label-orange: #e8401f;
  }
  html, body {
    margin: 0;
    padding: 0;
    width: 1200px;
    height: 1200px;
    overflow: hidden;
    background: var(--page-bg);
  }
  .flag-set {
    display: block;
    width: 1200px;
    height: 1200px;
  }
  .flag-outer { fill: var(--flag-orange); }
  .flag-trim { fill: var(--flag-brown); }
  .flag-panel-dark { fill: var(--panel-dark); }
  .brand-badge { fill: var(--badge-green); stroke: var(--flag-orange); stroke-width: 8; }
  .brand-name {
    font-family: "Rosario", sans-serif;
    font-size: 106px;
    fill: var(--flag-orange);
  }
  .brand-tagline {
    font-family: "Rosario", sans-serif;
    font-size: 28px;
    fill: var(--flag-orange);
    letter-spacing: 1px;
  }
  .menu-label {
    font-family: "Open Sans", sans-serif;
    font-weight: 700;
    font-size: 19px;
    fill: var(--label-orange);
  }
  .menu-brand {
    font-family: "Rosario", sans-serif;
    font-size: 22px;
    fill: var(--flag-orange);
  }
</style>
</head>
<body>
<svg class="flag-set" viewBox="0 0 1200 1200" xmlns="http://www.w3.org/2000/svg">
  <defs>
    <linearGradient id="creamFill" x1="0" y1="0" x2="0" y2="1">
      <stop offset="0" stop-color="var(--cream-top)"/>
      <stop offset="1" stop-color="var(--cream-bottom)"/>
    </linearGradient>
    <linearGradient id="pizzaTone" x1="0" y1="0" x2="1" y2="1">
      <stop offset="0" stop-color="#e9c48a"/>
      <stop offset="1" stop-color="#b8442c"/>
    </linearGradient>
    <linearGradient id="naniniTone" x1="0" y1="0" x2="1" y2="1">
      <stop offset="0" stop-color="#dcc7a0"/>
      <stop offset="1" stop-color="#a8552e"/>
    </linearGradient>
    <linearGradient id="bowlTone" x1="0" y1="0" x2="0" y2="1">
      <stop offset="0" stop-color="#dfe6c8"/>
      <stop offset="1" stop-color="#b23b22"/>
    </linearGradient>
    <linearGradient id="wrapTone" x1="0" y1="0" x2="1" y2="1">
      <stop offset="0" stop-color="#e6c68e"/>
      <stop offset="1" stop-color="#9c6a3a"/>
    </linearGradient>
    <clipPath id="menuPanelClip">
      <path d="M702,58 C812,78 890,168 890,370 L890,1142 C794,1104 736,1044 702,955 Z"/>
    </clipPath>
  </defs>

  <!-- Brand side -->
  <g class="flag flag-brand">
    <path class="flag-outer" d="M338,1180 L338,390 C338,220 430,50 570,20 L570,960 C540,1060 460,1140 338,1180 Z"/>
    <path class="flag-trim" d="M348,1166 L348,392 C348,232 436,68 560,34 L560,958 C532,1052 456,1126 348,1166 Z"/>
    <path fill="url(#creamFill)" d="M358,1150 L358,395 C358,244 444,86 550,50 L550,955 C524,1044 452,1112 358,1150 Z"/>

    <circle class="brand-badge" cx="454" cy="370" r="80"/>

    <text class="brand-name" transform="translate(414,472) rotate(90)">Marlowes</text>
    <text class="brand-tagline" transform="translate(506,490) rotate(90)">savor the flavor</text>
  </g>

  <!-- Menu side -->
  <g class="flag flag-menu">
    <path class="flag-outer" d="M680,28 C820,48 910,150 910,360 L910,1172 C790,1130 720,1060 680,960 Z"/>
    <path class="flag-trim" d="M691,43 C816,63 900,160 900,365 L900,1157 C792,1117 728,1052 691,958 Z"/>
    <path class="flag-panel-dark" d="M702,58 C812,78 890,168 890,370 L890,1142 C794,1104 736,1044 702,955 Z"/>

    <g clip-path="url(#menuPanelClip)">
      <ellipse role="img" aria-label="Photo of a naan pizza topped with cheese, chicken and red onion" fill="url(#pizzaTone)" cx="778" cy="186" rx="70" ry="52"/>
      <rect role="img" aria-label="Photo of a grilled nanini in a black basket" fill="url(#naniniTone)" x="706" y="300" width="174" height="158" rx="18"/>
      <rect role="img" aria-label="Photo of a rice bowl with slaw, spiced chicken and lime" fill="url(#bowlTone)" x="722" y="500" width="162" height="166" rx="14"/>
      <rect role="img" aria-label="Photo of a paratha wrap filled with meat and vegetables" fill="url(#wrapTone)" x="706" y="716" width="154" height="162" rx="40"/>
    </g>

    <text class="menu-label" x="729" y="274">NAAN PIZZA</text>
    <text class="menu-label" x="720" y="488">NANINI</text>
    <text class="menu-label" x="718" y="702">RICE BOWL</text>
    <text class="menu-label" x="778" y="905">PARATHA</text>
    <text class="menu-label" x="778" y="928">WRAP</text>

    <circle class="brand-badge" cx="816" cy="1006" r="60"/>
    <text class="menu-brand" x="816" y="1013" text-anchor="middle">Marlowes</text>
  </g>
</svg>
</body>
</html>
```